Business card for Mortgage broker business

I have already had the logo designed and am needing a great looking business card. My business focus is on servicing clients who may not be able to obtain finance through traditional lenders due to bad credit, short term employment or they just don't fit the banks profile. It needs to be professional, trust worthy but also have a caring fell about it.
I have provided files showing the green and black logo, the white logo(on white background so the file looks blank) and also a file with the white logo with a background of leaves that was made up which will probably be used for a website header.

Industry/Entity Type

Finance

Contact Information for Business Card

Marcus Dalby
Managing Director, Accredited Finance Broker(AFB)
Po Box 817, Pakenham VIC 3810
marcus@kestrelfunding.com.au
www.kestrelfunding.com.au
0438 216 507

Requirements
Nice to have
• I have added a picture of myself as I would like to see some designs with the pic in it, but I'm not sure if I want it on there with the logo's or just the logo's

```html
<!DOCTYPE html>
<html lang="en">
<head>
<meta charset="utf-8">
<title>Kestrel Funding – Business Card</title>
<link rel="stylesheet" href="https://fonts.googleapis.com/css2?family=Open+Sans:wght@400;600&display=swap">
<style>
  :root {
    --backdrop: #262626;
    --card-white: #ffffff;
    --brand-green: #0b6b38;
    --back-green: #076a37;
    --back-ink: #0d3f23;
    --text-grey: #4a4a4a;
    --rule-grey: #c9c9c9;
  }
  * { margin: 0; padding: 0; box-sizing: border-box; }
  html, body {
    width: 1200px; height: 987px; overflow: hidden;
    background: var(--backdrop);
    font-family: "Open Sans", Arial, sans-serif;
  }
  .stage { position: relative; width: 1200px; height: 987px; }
  .card {
    position: absolute; left: 293px; width: 615px; height: 352px;
    overflow: hidden;
  }
  .card-front { top: 130px; background: var(--card-white); }
  .card-back { top: 505px; background: var(--back-green); }

  .brand {
    position: absolute; left: 36px; top: 160px; width: 245px;
    display: flex; align-items: center; justify-content: center; gap: 10px;
  }
  .brand-dot {
    width: 13px; height: 13px; border-radius: 50%;
    background: var(--brand-green); flex: none;
  }
  .brand-name {
    font-size: 25px; font-weight: 600; color: var(--brand-green);
    letter-spacing: 0.3px; line-height: 1; white-space: nowrap;
  }

  .divider {
    position: absolute; left: 300px; top: 66px; width: 1px; height: 226px;
    background: var(--rule-grey);
  }

  .details { position: absolute; left: 324px; top: 68px; width: 272px; color: var(--text-grey); }
  .person-name {
    font-size: 22px; font-weight: 600; color: var(--brand-green);
    text-transform: uppercase; line-height: 1.1;
  }
  .person-role { font-size: 16px; text-transform: uppercase; margin-top: 2px; color: #333; }
  .address { font-size: 16px; line-height: 22px; margin-top: 12px; }
  .contact-list { list-style: none; margin-top: 6px; }
  .contact-list li {
    display: flex; align-items: center; gap: 8px;
    font-size: 16px; line-height: 23.5px; white-space: nowrap;
  }
  .contact-list svg { width: 15px; height: 15px; fill: var(--brand-green); flex: none; }

  .back-brand {
    position: absolute; left: 0; right: 0; top: 140px;
    display: flex; justify-content: center; align-items: center; gap: 14px;
  }
  .back-brand .brand-dot { width: 18px; height: 18px; background: var(--back-ink); }
  .back-brand .brand-name { font-size: 36px; color: var(--back-ink); }
  .back-web {
    position: absolute; left: 0; right: 0; top: 300px; text-align: center;
    font-size: 15px; letter-spacing: 6px; color: var(--back-ink);
  }
</style>
</head>
<body>
<main class="stage">
  <section class="card card-front">
    <div class="brand">
      <span class="brand-dot"></span>
      <span class="brand-name">Kestrel Funding</span>
    </div>
    <div class="divider"></div>
    <div class="details">
      <p class="person-name">Marcus Dalby</p>
      <p class="person-role">Managing Director</p>
      <p class="address">Po Box 817<br>Pakenham VIC 3810</p>
      <ul class="contact-list">
        <li><svg viewBox="0 0 16 16" aria-hidden="true"><path d="M3.6 1.5l2.3 2.6-1.2 1.9c.9 2 2.4 3.5 4.4 4.4l1.9-1.2 2.6 2.3-1.4 2.2C7.4 13.8 2.2 8.6 1.5 3z"/></svg>0438 216 507</li>
        <li><svg viewBox="0 0 16 16" aria-hidden="true"><path d="M4.5 1h7v14h-7zM5.8 2.5v9.5h4.4V2.5zM7.4 13h1.2v1H7.4z" fill-rule="evenodd"/></svg>0417 385 920</li>
        <li><svg viewBox="0 0 16 16" aria-hidden="true"><path d="M4 1h8v4H4zM1 6h14v7h-2v2H3v-2H1zM4.5 10v3.5h7V10z" fill-rule="evenodd"/></svg>03 5941 2276</li>
        <li><svg viewBox="0 0 16 16" aria-hidden="true"><path d="M1 3.5h14v9H1zM1.5 4l6.5 5 6.5-5v1.2L8 10.2 1.5 5.2z" fill-rule="evenodd"/></svg>marcus@kestrelfunding.com.au</li>
        <li><svg viewBox="0 0 16 16" aria-hidden="true"><path d="M8 1a7 7 0 1 0 0 14A7 7 0 0 0 8 1zm-1 2.5c1 1 .5 2-.5 2.5S5.5 8 6.5 9s1 2.5.5 3.5c-2.5-.5-4.3-2.6-4.3-5 0-1.8 1.9-3.5 4.3-4zm3 .2c1.5.5 2.8 1.9 3 3.6-1 .3-2-.3-2.5-1.2S9.6 4.5 10 3.7z"/></svg>www.kestrelfunding.com.au</li>
      </ul>
    </div>
  </section>

  <section class="card card-back">
    <div class="back-brand">
      <span class="brand-dot"></span>
      <span class="brand-name">Kestrel Funding</span>
    </div>
    <p class="back-web">www.kestrelfunding.com.au</p>
  </section>
</main>
</body>
</html>
```